Accountant website

Please design a accountant website for www.fenwaylodgeadvisory.com.au. This site is majorly out of date, and is not supported by modern browsers.

The style should use the reds from the design at dev.fenwaylodgeadvisory.com.au, and should be modern and make use of Slides (large content slides that the user scrolls through on the front page).

The content is largely already on the site, however happy to move some around to suit the modern design as required.

The dev.fenwaylodgeadvisory.com.au was a rough mock up that I have completed that the client is "happy" with the direction, however this needs a lot of polish and finishing touches, and I will accept designs that differ from this, but highly recommend that this is used as a guide.

Ready to be sliced PSD Only - HTML no required.

In all honesty, although I can technically do a lot of this, the polished finished I want for this site has eluded me in a few attempts, and therefore I am looking out there at you much more artistic people to finish (or redesign if required) this site.

Target Market(s)

Higher end Small - Medium Business

Industry/Entity Type

Accountant

Requirements
Must have
• Must use the logo from dev.fenwaylodgeadvisory.com.au use exactly the red colours as defined in this layout. A basic layout PSD (to get the colour etc) and the logo in ai format is attached to this project. Please ignore the SSL warning on the development site.

The final product does NOT have to be the same as shown on dev.fenwaylodgeadvisory.com.au however the red colour scheme must be used. The client DOES want the logo on the RIGHT.

Must have a front landing page design, and a page layout that considers the other page content (at least one separate PSD)
Nice to have
• I really am looking at a slide format for the front page simular to:

http://www.plumvine.com/au/
http://www.tidelockbox.com/

The attached photos should be used on the site. Was considering a rotating banner with these images are a watermark background on a solid Red header bar, but happy to be shown other options.
Should not have
• Please no "Pattern Goblin" submissions.

```html
<!DOCTYPE html>
<html lang="en">
<head>
<meta charset="utf-8">
<title>Fenway Lodge Advisory</title>
<link href="https://fonts.googleapis.com/css2?family=Oxygen:wght@400;700&family=Rajdhani:wght@500&family=Roboto:wght@400&display=swap" rel="stylesheet">
<style>
:root{
  --red:#c1272d;
  --red-deep:#7a0c0e;
  --hero-a:#b9575c;
  --hero-b:#d07a7c;
  --ink:#2b2b2b;
  --grey:#5f5f5f;
  --band:#f7f7f7;
  --footer:#262626;
  --white:#ffffff;
}
*{margin:0;padding:0;box-sizing:border-box}
html,body{width:1018px;height:1200px;overflow:hidden;background:var(--white)}
body{position:relative;font-family:"Roboto",Arial,sans-serif;color:var(--ink)}
.abs{position:absolute}

/* header */
.site-header{position:absolute;left:0;top:0;width:1018px;height:112px;background:var(--white)}
.brand{position:absolute;left:698px;top:26px;display:flex;align-items:center;gap:8px;font-family:"Oxygen",sans-serif;font-weight:700;font-size:21px;color:var(--ink);line-height:1.05}
.brand-mark{width:14px;height:14px;background:var(--red)}
.main-nav{position:absolute;left:134px;top:84px;display:flex;gap:19px;font-family:"Oxygen",sans-serif;font-size:12.5px;color:var(--ink)}
.main-nav .current{color:var(--red)}

/* hero */
.hero{position:absolute;left:0;top:112px;width:1018px;height:378px;overflow:hidden}
.hero-photo{position:absolute;inset:0;background:linear-gradient(90deg,var(--hero-a) 0%,#c46468 55%,var(--hero-b) 100%)}
.hero-title{position:absolute;left:0;width:1018px;top:16px;text-align:center;font-family:"Rajdhani",sans-serif;font-weight:500;font-size:42px;color:var(--white)}
.hero-sub{position:absolute;left:0;width:1018px;top:62px;text-align:center;font-family:"Rajdhani",sans-serif;font-weight:500;font-size:27px;color:var(--white)}
.hero-arrow{position:absolute;left:584px;top:96px}
.enquiry{position:absolute;left:398px;top:112px;width:220px;height:246px}
.enquiry svg{position:absolute;inset:0}
.field{position:absolute;left:24px;width:171px;background:var(--white);font-size:9.5px;color:#555;padding:9px 11px}
.go{position:absolute;left:97px;top:191px;width:26px;height:26px;border-radius:50%;background:var(--white);font-size:9.5px;color:#444;display:flex;align-items:center;justify-content:center}

/* features */
.features{position:absolute;left:0;top:490px;width:1018px;height:317px;background:var(--band);box-shadow:0 2px 2px rgba(0,0,0,.12)}
.hex-frame{position:absolute;width:116px;height:128px;background:#dcdcdc;clip-path:polygon(50% 0,100% 25%,100% 75%,50% 100%,0 75%,0 25%)}
.hex-photo{position:absolute;left:4px;top:4px;width:108px;height:120px;clip-path:polygon(50% 0,100% 25%,100% 75%,50% 100%,0 75%,0 25%)}
.feature-title{position:absolute;font-family:"Oxygen",sans-serif;font-weight:700;font-size:15.5px;color:var(--red)}
.feature-text{position:absolute;width:215px;font-size:10px;line-height:14px;color:var(--ink)}

/* about */
.about-title{position:absolute;left:134px;top:878px;font-family:"Oxygen",sans-serif;font-weight:700;font-size:23.5px;line-height:29px}
.about-title .lead{color:var(--red)}
.about-title .name{color:var(--grey)}
.about-text{position:absolute;left:578px;top:868px;width:306px;font-size:9.8px;line-height:13.7px;color:var(--ink)}

/* footer */
.site-footer{position:absolute;left:0;top:1014px;width:1018px;height:159px;background:var(--footer);color:var(--white)}
.col-title{position:absolute;top:18px;font-family:"Oxygen",sans-serif;font-weight:700;font-size:11.5px}
.quick-links{position:absolute;left:134px;top:37px;list-style:none;font-size:9.8px;line-height:17.6px}
.quick-links li::before{content:"•";margin-right:6px}
.divider{position:absolute;top:40px;width:1px;height:96px;background:linear-gradient(#262626,#8a8a8a,#262626)}
.quote{position:absolute;left:335px;top:42px;width:145px;font-size:9.8px;line-height:13px}
.quote-by{position:absolute;left:400px;top:97px;font-size:9.5px;letter-spacing:1px}
.quote-by small{font-size:7px}
.view-all{position:absolute;left:439px;top:127px;font-size:9.5px}
.social{position:absolute;left:558px;top:36px;list-style:none;font-size:9.8px}
.social li{display:flex;align-items:center;gap:11px;height:26.7px}
.social i{width:18px;height:18px;border-radius:50%;background:var(--white);display:block}
.footer-brand{position:absolute;left:713px;top:40px;font-family:"Oxygen",sans-serif;font-weight:700;font-size:21px;line-height:1.05;color:var(--white)}
.badge{position:absolute;left:713px;top:89px;width:49px;height:49px;border-radius:50%;background:var(--white)}
.legal{position:absolute;left:0;top:1173px;width:1018px;height:27px;background:var(--red);color:var(--white);font-size:10px;text-align:center;line-height:27px}
</style>
</head>
<body>

<header class="site-header">
  <div class="brand"><span class="brand-mark"></span><span>FENWAY LODGE<br>ADVISORY</span></div>
  <nav class="main-nav">
    <span class="current">About Us</span><span>Services</span><span>Working With Us</span><span>Testimonials</span><span>Article Of The Moment</span><span>Client Login</span>
  </nav>
</header>

<section class="hero">
  <div class="hero-photo" role="img" aria-label="Red-tinted photo of a woman in a red dress seated on a harbour pier with city buildings behind"></div>
  <h1 class="hero-title">Business can be hard</h1>
  <p class="hero-sub">But we make detailed analysis of your finances easy</p>
  <svg class="hero-arrow" width="44" height="52" viewBox="0 0 44 52" fill="none" stroke="#fff" stroke-width="2" stroke-linecap="round">
    <path d="M38 2 C42 24 30 40 6 46"/><path d="M14 36 L5 46 L18 49"/>
  </svg>
  <form class="enquiry">
    <svg width="220" height="246" viewBox="0 0 220 246">
      <polygon points="110,12 208,68 208,178 110,234 12,178 12,68" fill="#7a0c0e" stroke="#7a0c0e" stroke-width="24" stroke-linejoin="round"/>
    </svg>
    <div class="field" style="top:66px;height:30px">Name:</div>
    <div class="field" style="top:104px;height:30px">Email:</div>
    <div class="field" style="top:142px;height:39px">Message:</div>
    <div class="go">GO</div>
  </form>
</section>

<section class="features">
  <div class="hex-frame" style="left:132px;top:22px"><div class="hex-photo" style="background:linear-gradient(#c9d4df,#8c9aa8)" role="img" aria-label="Silhouette of two figures against a cloudy sky"></div></div>
  <h2 class="feature-title" style="left:265px;top:53px">Believing in the here and now</h2>
  <p class="feature-text" style="left:266px;top:82px">There are many variations of passages of lorem Ipsum available, but the majority have alteration in some form.</p>

  <div class="hex-frame" style="left:529px;top:22px"><div class="hex-photo" style="background:linear-gradient(#f1f1f1,#9a9a9a)" role="img" aria-label="Fountain pen signing a document beside a calculator"></div></div>
  <h2 class="feature-title" style="left:662px;top:53px">Monthly Billing</h2>
  <p class="feature-text" style="left:663px;top:82px">There are many variations of passages of lorem Ipsum available, but the majority have alteration in some form.</p>

  <div class="hex-frame" style="left:132px;top:166px"><div class="hex-photo" style="background:linear-gradient(#f5f5f5,#bdbdbd)" role="img" aria-label="Illustration of a businessman with an hourglass for a head"></div></div>
  <h2 class="feature-title" style="left:265px;top:197px">Your Place, In your time</h2>
  <p class="feature-text" style="left:266px;top:226px">There are many variations of passages of lorem Ipsum available, but the majority have alteration in some form.</p>

  <div class="hex-frame" style="left:529px;top:166px"><div class="hex-photo" style="background:linear-gradient(#e9c49a,#b07a4e)" role="img" aria-label="Smiling support agent wearing a headset"></div></div>
  <h2 class="feature-title" style="left:662px;top:197px">We will actually call you back</h2>
  <p class="feature-text" style="left:663px;top:226px">There are many variations of passages of lorem Ipsum available, but the majority have alteration in some form.</p>
</section>

<section>
  <h2 class="about-title"><span class="lead">Getting to Know</span><br><span class="name">Fenway Lodge Advisory</span></h2>
  <div class="hex-frame" style="left:458px;top:858px;width:93px;height:104px"><div class="hex-photo" style="width:87px;height:98px;left:3px;top:3px;background:linear-gradient(#b9c3cc,#6f5a4c)" role="img" aria-label="Portrait of the firm's director"></div></div>
  <p class="about-text">Fenway Lodge Advisory aims to service the needs of its clients by focusing on the present rather than reporting on historical figures. We recognise that business owners benefit from regular contact with their accountant. One who undertakes a hands on approach in working with business owners to improve their business.</p>
</section>

<footer class="site-footer">
  <h3 class="col-title" style="left:134px">Quick Links</h3>
  <ul class="quick-links">
    <li>About Us</li><li>Services</li><li>Working With Us</li><li>Testimonials</li><li>Article Of The Moment</li><li>Client Login</li>
  </ul>
  <span class="divider" style="left:286px"></span>
  <h3 class="col-title" style="left:327px">Testimonials</h3>
  <p class="quote">“Lorem ipsum dolor sit amet, tetuer adipiscing elit, sed diam nonum sum ipsum Lorem ipsum dolor sit amet.”</p>
  <p class="quote-by">Lorem, <small>DIRECTOR</small></p>
  <span class="view-all">View All</span>
  <span class="divider" style="left:516px"></span>
  <h3 class="col-title" style="left:558px">Follow Us On</h3>
  <ul class="social">
    <li><i></i>Friendbook</li><li><i></i>Chirper</li><li><i></i>Circles +</li><li><i></i>Linkwork</li>
  </ul>
  <span class="divider" style="left:673px"></span>
  <div class="footer-brand">FENWAY LODGE<br>ADVISORY</div>
  <span class="badge"></span>
</footer>
<p class="legal">© 2013 Fenway Lodge Advisory. All Rights Reserved.</p>

</body>
</html>
```